Design a "healthy, happy dog and cat" cheque/check background

I am looking for a few design concepts featuring a happy healthy dog and cat, that will be used as the background of a paper cheque/check.

This will require Photoshop and stock photos.

Here is the design brief: https://files.brieflocker.net/d/8Xq3LmTz0wRcYvNb2KpHsJfGdUeAi5oWnQ/view?share=link

Colors

Requirements
Must have
• A happy dog and cat the main focus within the "empty" central part of the cheque/check, and a complementary background for the rest of the cheque, following the design guidelines in the attached google doc.

```html
<!DOCTYPE html>
<html lang="en">
<head>
<meta charset="utf-8">
<title>Healthy, Happy Dog and Cat Cheque Designs</title>
<link rel="stylesheet" href="https://fonts.googleapis.com/css2?family=Arimo:wght@400;700&family=Share+Tech+Mono&family=Source+Sans+3:wght@400&display=swap">
<style>
  :root {
    --ink: #111111;
    --rule: #3a3a3a;
    --edge-blue: #12b5f0;
    --sky-top: #a9cdf7;
    --sky-bottom: #cfe6fb;
    --wood-light: #eeeeee;
    --wood-mid: #dcdcdc;
    --box: #ffffff;
    --label-grey: #555555;
    --page: #ffffff;
  }
  * { box-sizing: border-box; margin: 0; padding: 0; }
  html, body { width: 1200px; height: 1200px; overflow: hidden; background: var(--page); }
  body { position: relative; font-family: "Arimo", Arial, sans-serif; color: var(--ink); }

  .design { position: absolute; left: 0; width: 1200px; }
  .design--sky { top: 20px; }
  .design--wood { top: 656px; }

  .cheque {
    position: absolute; left: 24px; top: 0; width: 1176px; height: 392px;
    border-bottom: 4px solid var(--edge-blue); overflow: hidden;
  }
  .cheque--sky { background: linear-gradient(180deg, var(--sky-top), var(--sky-bottom)); }
  .cheque--wood {
    background: repeating-linear-gradient(90deg, var(--wood-light) 0 38px, var(--wood-mid) 38px 40px, var(--wood-light) 40px 96px);
  }

  .cheque__photo { position: absolute; top: 0; height: 388px; }
  .cheque--sky .cheque__photo {
    left: 330px; width: 690px;
    background: radial-gradient(ellipse at 40% 55%, #e9c98f 0%, #f0dcc0 38%, rgba(236,226,220,0.6) 62%, rgba(207,230,251,0) 80%);
  }
  .cheque--wood .cheque__photo {
    left: 340px; width: 610px;
    background: radial-gradient(ellipse at 50% 50%, #d8b99a 0%, #e6d3c2 40%, rgba(225,215,210,0.5) 65%, rgba(238,238,238,0) 82%);
  }

  .owner { position: absolute; left: 34px; top: 42px; line-height: 21px; }
  .owner__title { font-weight: 700; font-size: 22px; letter-spacing: 0.5px; }
  .owner__line { font-size: 19px; }

  .cheque__number { position: absolute; left: 1000px; top: 26px; font-weight: 700; font-size: 26px; }

  .date__label { position: absolute; left: 760px; top: 90px; font-size: 20px; }
  .date__boxes { position: absolute; left: 826px; top: 70px; display: flex; gap: 2.6px; }
  .date__box { width: 37px; height: 36px; background: var(--box); }
  .date__codes { position: absolute; left: 826px; top: 110px; display: flex; gap: 2.6px; }
  .date__code { width: 37px; text-align: center; font-size: 15px; }

  .payee__label { position: absolute; left: 32px; top: 170px; font-size: 16px; line-height: 14px; }
  .rule { position: absolute; height: 1px; background: var(--rule); }
  .rule--payee { left: 32px; top: 202px; width: 866px; }
  .rule--payee-tick { position: absolute; left: 898px; top: 170px; width: 1px; height: 33px; background: var(--rule); }
  .rule--words { left: 32px; top: 256px; width: 848px; }
  .rule--words-slash { position: absolute; left: 880px; top: 220px; width: 1px; height: 38px; background: var(--rule); transform: skewX(-14deg); }
  .rule--memo { left: 32px; top: 378px; width: 530px; }
  .rule--sign { left: 662px; top: 378px; width: 413px; }

  .amount__sign { position: absolute; left: 924px; top: 168px; font-size: 30px; }
  .amount__box { position: absolute; left: 948px; top: 154px; width: 194px; height: 48px; background: var(--box); }
  .amount__words { position: absolute; left: 894px; top: 232px; font-size: 16px; }

  .bank { position: absolute; left: 34px; top: 266px; }
  .bank__mark { position: absolute; left: 14px; top: 12px; width: 56px; height: 56px; border-radius: 50%; background: var(--ink); }
  .bank__text { position: absolute; left: 96px; top: 12px; width: 380px; font-size: 18px; line-height: 19px; letter-spacing: 1px; }
  .bank__name { font-weight: 700; font-size: 19px; }

  .company { position: absolute; left: 784px; top: 312px; font-size: 15px; }
  .memo__label { position: absolute; left: 37px; top: 362px; font-size: 13px; }

  .security { position: absolute; left: 1136px; top: 252px; width: 32px; height: 136px; border: 1px solid var(--ink); background: rgba(255,255,255,0.4); }
  .security__text { position: absolute; left: 2px; top: 4px; width: 72px; height: 26px; font-size: 8px; line-height: 9px; transform-origin: 0 0; transform: translate(2px, 72px) rotate(-90deg); }
  .security__icon { position: absolute; left: 6px; top: 78px; }
  .security__seal { position: absolute; left: 8px; top: 118px; width: 14px; height: 12px; background: var(--ink); }

  .micr { position: absolute; left: 54px; top: 432px; font-family: "Share Tech Mono", monospace; font-size: 30px; letter-spacing: 3px; }
  .design__label { position: absolute; left: 992px; top: 446px; font-family: "Source Sans 3", sans-serif; font-size: 32px; letter-spacing: 4px; color: var(--label-grey); }
  .band { position: absolute; left: 0; top: 506px; width: 1200px; height: 18px; background: var(--edge-blue); }
  .design--wood .band { top: 508px; height: 16px; }
</style>
</head>
<body>

<section class="design design--sky">
  <div class="cheque cheque--sky">
    <div class="cheque__photo" role="img" aria-label="Photo of a smiling golden retriever, a young girl and a white and ginger cat"></div>

    <div class="owner">
      <div class="owner__title">Maple Row Cheques Personal Cheque</div>
      <div class="owner__line">27 Orchard Lane</div>
      <div class="owner__line">Brookfield, Ontario K0K 2L0</div>
    </div>
    <div class="cheque__number">101</div>

    <div class="date__label">DATE</div>
    <div class="date__boxes"><span class="date__box"></span><span class="date__box"></span><span class="date__box"></span><span class="date__box"></span><span class="date__box"></span><span class="date__box"></span><span class="date__box"></span><span class="date__box"></span></div>
    <div class="date__codes"><span class="date__code">D</span><span class="date__code">D</span><span class="date__code">M</span><span class="date__code">M</span><span class="date__code">Y</span><span class="date__code">Y</span><span class="date__code">Y</span><span class="date__code">Y</span></div>

    <div class="payee__label">PAY TO THE<br>ORDER OF</div>
    <div class="rule rule--payee"></div><div class="rule--payee-tick"></div>
    <div class="amount__sign">$</div>
    <div class="amount__box"></div>
    <div class="rule rule--words"></div><div class="rule--words-slash"></div>
    <div class="amount__words">100 DOLLARS</div>

    <div class="bank">
      <span class="bank__mark"></span>
      <div class="bank__text">
        <div class="bank__name">Your Financial Institution</div>
        <div>200 Finance Avenue</div>
        <div>Your City, Your Province A1B 2CS</div>
      </div>
    </div>
    <div class="company">Optional Company Name</div>
    <div class="memo__label">MEMO</div>
    <div class="rule rule--memo"></div>
    <div class="rule rule--sign"></div>

    <div class="security">
      <div class="security__text">Details on Back<br>Détails au Verso</div>
      <svg class="security__icon" width="18" height="22" viewBox="0 0 18 22"><path d="M4 10V6a5 5 0 0 1 10 0v4" fill="none" stroke="#111" stroke-width="2"/><rect x="1" y="10" width="16" height="11" fill="none" stroke="#111" stroke-width="2"/><path d="M9 18v-5M7 15l2-2 2 2" fill="none" stroke="#111" stroke-width="1.5"/></svg>
      <span class="security__seal"></span>
    </div>
  </div>
  <div class="micr">⑈101⑈ ⑆12345⑉678⑆ 12345⑉6789⑈</div>
  <div class="design__label">DESIGN 3</div>
  <div class="band"></div>
</section>

<section class="design design--wood">
  <div class="cheque cheque--wood">
    <div class="cheque__photo" role="img" aria-label="Photo of a laughing girl hugging a tan puppy and a Siamese cat"></div>

    <div class="owner">
      <div class="owner__title">Maple Row Cheques Personal Cheque</div>
      <div class="owner__line">27 Orchard Lane</div>
      <div class="owner__line">Brookfield, Ontario K0K 2L0</div>
    </div>
    <div class="cheque__number">101</div>

    <div class="date__label">DATE</div>
    <div class="date__boxes"><span class="date__box"></span><span class="date__box"></span><span class="date__box"></span><span class="date__box"></span><span class="date__box"></span><span class="date__box"></span><span class="date__box"></span><span class="date__box"></span></div>
    <div class="date__codes"><span class="date__code">D</span><span class="date__code">D</span><span class="date__code">M</span><span class="date__code">M</span><span class="date__code">Y</span><span class="date__code">Y</span><span class="date__code">Y</span><span class="date__code">Y</span></div>

    <div class="payee__label">PAY TO THE<br>ORDER OF</div>
    <div class="rule rule--payee"></div><div class="rule--payee-tick"></div>
    <div class="amount__sign">$</div>
    <div class="amount__box"></div>
    <div class="rule rule--words"></div><div class="rule--words-slash"></div>
    <div class="amount__words">100 DOLLARS</div>

    <div class="bank">
      <span class="bank__mark"></span>
      <div class="bank__text">
        <div class="bank__name">Your Financial Institution</div>
        <div>200 Finance Avenue</div>
        <div>Your City, Your Province A1B 2CS</div>
      </div>
    </div>
    <div class="company">Optional Company Name</div>
    <div class="memo__label">MEMO</div>
    <div class="rule rule--memo"></div>
    <div class="rule rule--sign"></div>

    <div class="security">
      <div class="security__text">Details on Back<br>Détails au Verso</div>
      <svg class="security__icon" width="18" height="22" viewBox="0 0 18 22"><path d="M4 10V6a5 5 0 0 1 10 0v4" fill="none" stroke="#111" stroke-width="2"/><rect x="1" y="10" width="16" height="11" fill="none" stroke="#111" stroke-width="2"/><path d="M9 18v-5M7 15l2-2 2 2" fill="none" stroke="#111" stroke-width="1.5"/></svg>
      <span class="security__seal"></span>
    </div>
  </div>
  <div class="micr">⑈101⑈ ⑆12345⑉678⑆ 12345⑉6789⑈</div>
  <div class="design__label">DESIGN 4</div>
  <div class="band"></div>
</section>

</body>
</html>
```